Vorlen - Customer Experience Software Company Web Design

*****UPDATE*****
We've been getting a lot of corporate designs through. Unfortunately this is not what we are looking for. We would like our brand to be more approachable and for the look and feel to to be a bit more fun.
Also the best designs we have received so far have followed the "less is more" approach. Im hoping any news designs will take these aspects into account.
*****************

Background:

Vorlen is a Customer Experience Technology company. We equip business and technology teams with the frameworks, tools and services to help them create compelling experiences for their customers.

Our flagship product - Vorlen CX is an open-source customer experience application framework – it enables organisation to build highly differentiated business applications to deliver compelling experiences to your customers.

Vorlen CX is designed for innovators who understand that unlocking opportunity in today’s competitive marketplace is driven by delivering a better customer experience.

Task:

We are looking for a web design (we need PSD, no HTML/CSS) for our company site through which to launch our customer experience framework product. The site will be also used as a support site, so the functional aspect of the site is as important as the visual impact for sales.

In order to help us conceptualise ideas and content we have drafted a temporary website using a standard wordpress theme (please see details below). Now we have a general idea of our requirements we like we would like to take it to the next level and get some designs with that professional edge.

Our target market are Enterprise organisations - that is senior members of the business & technology teams (Business General Managers, CTO’s, CIO’s, and Senior Architects and Senior Developers). We want something clean & fresh which is DIFFERENT from the typical corporate technology websites out there. We would like to be seen as more approachable than most large technology companies.

Words we would like to use to describe the finished design:
• Clean (we’re thinking white background with one or two key colours)
• Fresh
• Light
• Modern
• Less is more
• Web 2.0
• Fun but professional (aimed at Enterprise/Large organisations)
• Bold, clear call to action – e.g. Live Demo & Download
• Readable (but Sans Serif)

As we’re a Customer Experience company, the usability of the site is critical. The site must be functional, intuitive & easy to navigate. We want to keep the number of user clicks to the bare minimum possible.

Other aspects, which we would like to incorporate into the site
• Home Page banner slider
• Client logon
• Newsletter sign up
• Social media links – Facebook, LinkedIn (for starters)
• Rich footer links

Some websites we like
• http://brightpanelworks.example - clean, light, modern & intuitive
• http://www.tamsoledrik.example - bold, clear messaging
• http://www.opengridhub.example/markup/emblem - punchy, colourful
• http://postwren.example/ - modern, clear messaging, colourful, rich footer area

Target Market(s)

Enterprise organisations - that is senior members of the business & technology teams (Business General Managers, CTO’s, CIO’s, Senior Devs)

Industry/Entity Type

Business

Requirements
Must have
• - Design Specs: Accepted file formats: During the design phase adobe PSD or JPEG are OK (if you need to upload files), but for the handover we'll need PSD only with all the original layers.
- The width needs to be a size that will work with every size computer screen
- Need to use cross-platform compatible font
- The graphic elements used for the design must be copyright free

Current test site
- URL http://vorlen.example/wp-admin
- username: artmarket
- password: artmarket

IMPORTANT NOTE REGARDING OUR CURRENT TEST SITE:

This is a very basic version of a site to help us generate requirements. This design is only a starting point/input and is not locked in stone i.e. we do not simply want this site simply tweaked around the edges.

We are looking for you to use all of your graphic design skills and experience to create a truly awesome site design!

```html
<!DOCTYPE html>
<html lang="en">
<head>
<meta charset="utf-8">
<title>Vorlen — The Customer Experience Framework</title>
<link rel="stylesheet" href="https://fonts.googleapis.com/css2?family=Ubuntu:wght@400;500&family=Roboto:wght@300;400&family=Roboto+Condensed:wght@400;500&family=Arimo&display=swap">
<style>
  :root {
    --night: #262a33;
    --black: #050505;
    --sky: #9dd6f2;
    --sky-link: #8fd0f0;
    --rule: #b9b9b9;
    --paper: #e9e8e6;
    --ink: #333840;
    --heading-blue: #3a4ea0;
    --body-grey: #666a70;
    --soft-white: #e6e8ec;
    --red-top: #f36b45;
    --red-bottom: #e2352b;
    --blue-top: #2f7fd6;
    --blue-bottom: #243f9a;
  }
  * { margin: 0; padding: 0; box-sizing: border-box; }
  html, body { width: 1200px; height: 1029px; overflow: hidden; background: var(--night); }
  .page { position: relative; width: 1200px; height: 1029px; overflow: hidden; font-family: "Ubuntu", sans-serif; }
  .abs { position: absolute; }

  /* header */
  .site-header { left: 0; top: 0; width: 1200px; height: 110px; background: var(--night); }
  .brand-name { left: 219px; top: 12px; font-family: "Roboto", sans-serif; font-weight: 400; font-size: 57px; line-height: 1; color: #fff; letter-spacing: -1px; }
  .brand-tagline { left: 223px; top: 70px; font-size: 13.5px; color: #fff; }
  .account-links { left: 891px; top: 16px; font-size: 10px; color: #fff; letter-spacing: .3px; padding-bottom: 4px; border-bottom: 2px solid #8a8e96; }
  .account-links span { margin: 0 6px; }
  .main-nav { right: 219px; top: 71px; display: flex; gap: 22px; font-size: 15.5px; color: #d8dadf; }
  .main-nav .is-current { color: var(--sky-link); }
  .header-rule { left: 0; top: 110px; width: 1200px; height: 4px; background: var(--rule); }

  /* hero */
  .hero { left: 0; top: 114px; width: 1200px; height: 375px; background: var(--sky); }
  .hero-title { left: 222px; top: 56px; font-family: "Roboto", sans-serif; font-weight: 300; font-size: 68px; line-height: 75px; color: var(--ink); }
  .hero-subtitle { left: 224px; top: 208px; font-family: "Roboto Condensed", sans-serif; font-size: 41px; color: var(--ink); }
  .btn-demo-large { left: 224px; top: 276px; width: 128px; height: 38px; border-radius: 4px; background: linear-gradient(var(--red-top), var(--red-bottom)); color: #fff; font-family: "Roboto Condensed", sans-serif; font-weight: 500; font-size: 20px; display: flex; align-items: center; justify-content: center; }
  .slider-arrow { top: 141px; }
  .product-visual { left: 617px; top: 43px; width: 363px; height: 310px; border-radius: 8px; background: linear-gradient(#1b1b1d 0%, #2a2b2f 70%, #c9ccd0 71%, #9aa0a6 100%); }
  .hero-rule { left: 0; top: 489px; width: 1200px; height: 5px; background: var(--rule); }

  /* intro */
  .intro { left: 0; top: 494px; width: 1200px; height: 303px; background: var(--paper); }
  .intro-heading { left: 222px; top: 30px; font-size: 27px; line-height: 32px; color: var(--heading-blue); font-weight: 400; }
  .intro-copy { left: 223px; top: 110px; width: 518px; font-family: "Arimo", sans-serif; font-size: 12.5px; line-height: 16.7px; color: var(--body-grey); }
  .btn-grey { left: 219px; top: 240px; width: 95px; height: 28px; border-radius: 3px; background: linear-gradient(#f3f3f3, #bdbdbd); color: #333; font-family: "Roboto Condensed", sans-serif; font-size: 13.5px; display: flex; align-items: center; justify-content: center; }
  .product-card { left: 767px; top: 18px; width: 216px; height: 266px; border-radius: 6px; background: var(--sky); }
  .product-card p { position: absolute; left: 21px; top: 20px; width: 190px; font-family: "Roboto", sans-serif; font-size: 15.5px; line-height: 22.3px; color: #4b5058; }
  .product-card strong { font-weight: 400; color: #1b1e24; }
  .btn-blue { top: 222px; height: 28px; border-radius: 3px; background: linear-gradient(var(--blue-top), var(--blue-bottom)); color: #fff; font-family: "Roboto Condensed", sans-serif; font-size: 13.5px; display: flex; align-items: center; justify-content: center; }
  .intro-rule { left: 0; top: 797px; width: 1200px; height: 6px; background: var(--rule); }

  /* footer */
  .site-footer { left: 0; top: 803px; width: 1200px; height: 175px; background: var(--night); color: #fff; }
  .footer-list { list-style: none; font-size: 11.2px; }
  .footer-list li { height: 21.8px; position: relative; padding-left: 14px; }
  .footer-list li::before { content: ""; position: absolute; left: 0; top: 3px; width: 5px; height: 5px; border-radius: 50%; background: #fff; }
  .footer-list.is-root li { padding-left: 14px; }
  .footer-heading { font-size: 19px; font-weight: 400; color: var(--sky-link); }
  .social-tile { top: 71px; width: 21px; height: 21px; border-radius: 4px; background: #d9dbde; }
  .email-field { left: 802px; top: 71px; width: 182px; height: 31px; border-radius: 3px; background: var(--soft-white); color: #333; font-size: 13px; padding: 9px 13px; }
  .btn-signup { left: 890px; top: 114px; width: 93px; height: 28px; border-radius: 3px; background: linear-gradient(var(--red-top), var(--red-bottom)); color: #fff; font-size: 14px; font-weight: 500; display: flex; align-items: center; justify-content: center; }

  .legal-bar { left: 0; top: 978px; width: 1200px; height: 51px; background: var(--black); }
  .legal-bar p { position: absolute; left: 218px; top: 14px; font-size: 11px; color: #fff; }
  .legal-bar span { margin: 0 7px; }
</style>
</head>
<body>
<div class="page">

  <header class="site-header abs">
    <div class="brand-name abs">Vorlen</div>
    <div class="brand-tagline abs">The Customer Experience Framework</div>
    <div class="account-links abs">LOGIN<span>|</span>REGISTER</div>
    <nav class="main-nav abs">
      <span class="is-current">Home</span><span>Products</span><span>Support</span><span>Blog</span><span>About</span><span>Contact</span>
    </nav>
  </header>
  <div class="header-rule abs"></div>

  <section class="hero abs">
    <h1 class="hero-title abs" style="font-weight:300">Customer<br>Experience</h1>
    <div class="hero-subtitle abs">Application Framework</div>
    <div class="btn-demo-large abs">LIVE DEMO</div>
    <svg class="slider-arrow abs" style="left:160px" width="24" height="36" viewBox="0 0 24 36"><polyline points="22,1 2,18 22,35" fill="none" stroke="#555b63" stroke-width="2"/></svg>
    <svg class="slider-arrow abs" style="left:1017px" width="24" height="36" viewBox="0 0 24 36"><polyline points="2,1 22,18 2,35" fill="none" stroke="#555b63" stroke-width="2"/></svg>
    <div class="product-visual abs" role="img" aria-label="Desktop monitor showing the analytics dashboard of the framework"></div>
  </section>
  <div class="hero-rule abs"></div>

  <section class="intro abs">
    <h2 class="intro-heading abs">Create compelling experiences<br>for your customers</h2>
    <p class="intro-copy abs">“Sed ut perspiciatis unde omnis iste natus error sit voluptatem accusantium doloremque laudantium, totam rem aperiam, eaque ipsa quae ab illo inventore veritatis et quasi architecto beatae vitae dicta sunt explicabo. Nemo enim ipsam voluptatem quia voluptas sit aspernatur aut odit aut fugit, sed quia consequuntur magni dolores eos qui ratione voluptatem sequi nesciunt. Neque porro quisquam est, qui dolorem ipsum quia dolor sit amet, consectetur, adipisci velit, sed quia non numquam eius modi tempora incidunt ut labore et dolore magnam aliquam quaerat voluptatem. Ut enim ad minima veniam, quis.</p>
    <div class="btn-grey abs">Read More</div>
    <aside class="product-card abs">
      <p><strong>Vorlen CX</strong> is a customer experience application framework - it enables you to build highly differentiated business applications to deliver compelling experiences to your customers</p>
      <div class="btn-blue abs" style="left:17px;width:80px">Download</div>
      <div class="btn-blue abs" style="left:119px;width:81px">Live Demo</div>
    </aside>
  </section>
  <div class="intro-rule abs"></div>

  <footer class="site-footer abs">
    <ul class="footer-list is-root abs" style="left:216px;top:35px">
      <li>Home</li><li>Products</li><li>Support</li><li>Blog</li><li>About</li><li>Contact</li>
    </ul>
    <h3 class="footer-heading abs" style="left:320px;top:36px">Getting Started</h3>
    <ul class="footer-list abs" style="left:325px;top:71px">
      <li>Demo</li><li>Documentation</li><li>Download</li>
    </ul>
    <h3 class="footer-heading abs" style="left:511px;top:36px">Support</h3>
    <ul class="footer-list abs" style="left:511px;top:71px">
      <li>Contact Us</li><li>Vorlen Services</li><li>Vorlen Support</li>
    </ul>
    <h3 class="footer-heading abs" style="left:640px;top:36px">Follow Us</h3>
    <div class="social-tile abs" style="left:642px" role="img" aria-label="Social network link"></div>
    <div class="social-tile abs" style="left:670px" role="img" aria-label="Social network link"></div>
    <div class="social-tile abs" style="left:698px" role="img" aria-label="Social network link"></div>
    <div class="social-tile abs" style="left:726px" role="img" aria-label="Social network link"></div>
    <h3 class="footer-heading abs" style="left:800px;top:36px">Newsletter Sign-up</h3>
    <div class="email-field abs">Email:</div>
    <div class="btn-signup abs">Sign Up</div>
  </footer>

  <div class="legal-bar abs">
    <p>© Copyright 2012<span>|</span>Vorlen<span>|</span>All rights reserved.</p>
  </div>

</div>
</body>
</html>
```